TLKompass online header

We need a header for our online internal company newsletter/blogsite. It is called the TLKompass which is a contraction between TLK (the department associated) and the word Gazette.
We want to have a new modern design for the header that should say "TLKompass" or "TLKompass online" (there used to be a paper version) in a nice artistic modern friendly inviting way. Sort of like a newspaper header.
There could be an optional text line that says "Every story that counts" or something like that.
Target Market(s)
Consulting professionals in the area of mathematics, econometrics and IT
Industry/Entity Type
It Company
Logo Text
TLKompass
Colors
Look and feel

```html
<!DOCTYPE html>
<html lang="en">
<head>
<meta charset="utf-8">
<title>TLKompass – Every story that counts</title>
<link rel="stylesheet" href="https://fonts.googleapis.com/css2?family=Nunito:wght@800&display=swap">
<style>
  :root {
    --paper-light: #efefef;
    --paper-mid: #dcdcdc;
    --paper-shade: #cdcdcd;
    --title-ink: #606060;
    --tagline-ink: #3c3c3c;
  }
  * { margin: 0; padding: 0; box-sizing: border-box; }
  html, body {
    width: 1200px;
    height: 325px;
    overflow: hidden;
    background: var(--paper-light);
  }
  .header-banner {
    position: relative;
    width: 1200px;
    height: 325px;
    overflow: hidden;
  }
  .paper-texture {
    position: absolute;
    inset: 0;
    background:
      radial-gradient(ellipse 420px 200px at 180px 260px, var(--paper-shade), transparent 70%),
      radial-gradient(ellipse 380px 180px at 1050px 170px, var(--paper-mid), transparent 70%),
      radial-gradient(ellipse 500px 160px at 620px 40px, #f6f6f6, transparent 70%),
      linear-gradient(160deg, #e6e6e6 0%, var(--paper-light) 45%, #e2e2e2 100%);
  }
  .masthead {
    position: absolute;
    left: 0;
    right: 0;
    top: 130px;
    text-align: center;
    font-family: "Nunito", sans-serif;
    font-weight: 800;
  }
  .masthead-title {
    font-size: 62px;
    font-weight: 800;
    line-height: 1;
    color: var(--title-ink);
    text-transform: uppercase;
  }
  .masthead-tagline {
    margin-top: 8px;
    font-size: 17px;
    font-weight: 800;
    line-height: 1;
    letter-spacing: 1.5px;
    color: var(--tagline-ink);
    text-transform: uppercase;
  }
</style>
</head>
<body>
  <header class="header-banner">
    <div class="paper-texture" role="img" aria-label="Crumpled light grey paper texture background"></div>
    <div class="masthead">
      <h1 class="masthead-title">TLKompass</h1>
      <p class="masthead-tagline">Every story that counts</p>
    </div>
  </header>
</body>
</html>
```